Modern Informational OBGYN website

Looking for a modern Wordpress website for a general OBGYN practice in Florida with a specialty in High Risk Obstetrics. We had an old Joomla website that crashed and we lost most of the files. It was over 10 years old and needed a refresh anyway.

Our practice serves a multicultural patient population (white, black, Spanish and Indian) and we would like our website to reflect that diversity. Our company colors are sunshine yellow (#ECBF6D) often combined with black, white and steel blue (#7191BE) in the "life" part of our logo (attached) depending on the background. Our tagline is "We're specialist in You!" Overall the site should have a clean modern yet comfortable feel. One that portrays friendliness and competence. At least 6 pages (Home, Obstetrics, Gynecology, News, Patient Education and Resources). Rotating stock pictures or videos are fine for the headers of the pages if the design you're considering calls for it. Interesting and creative use of typography and icons are encouraged.

The home page should have a call to action to schedule an appointment as well as a link to our patient portal. Other than the home and news pages, the other pages should have a similar look and feel. The home page should have sections on "About Us", "Medical Staff" (with pictures and brief bio for 2 male doctors, 2 female midwives and 1 female nurse practitioner), "Services" and "Location". The news page will be a closed blog that will not allow comments or responses. Both the obstetrics and the gynecology pages will have an educational blurb on the respective topics followed by a list of our services for each topic. Would be nice on the obstetrics page to have information and graphics changes that occur during each trimester (but not necessary). The resource page will have sections on at least "Office Forms", Office Policies", "OB Guide" each with multiple downloadable PDF's. Also a section on "Insurance" with a list of all the major insurance plans that we take with links to their company websites. The address, link and map to our hospital and their website can also go on this page. The Patient Education Page can be broken into 3 sections Obstetrics, Gynecology which both will have definition of medical disorders followed by FAQ's and "Helpful Links" which would have links to other website for medical information.

That's all that I can think of right now. The above is to help guide you but I am flexible, if the website design dictates a better flow of information. Looking forward to seeing what you can come up with. Down the road, I will be looking to the winning designer to produce matching brochures, full, half and quarter page media ads to have on hand for the practices further needs.

Target Market(s)

Women looking medical services

Industry/Entity Type

Medical

Coding

Coded - Design and coding required

Number of Pages Required

5+ page

Font styles to use
Sans Serif
Script

Colors

Designer to choose colors to be used in the design.

Requirements
Must have
• None. See projects description for suggestions
Nice to have
• infographics like information on stages of pregnancy on the obstetrics page

```html
<!DOCTYPE html>
<html lang="en">
<head>
<meta charset="utf-8">
<title>Dawnvale OB/GYN Services</title>
<link href="https://fonts.googleapis.com/css2?family=Montserrat:wght@400;500;600;700&family=Playfair+Display:wght@700;900&display=swap" rel="stylesheet">
<style>
:root{
  --sun:#F0B22A;
  --ink:#1b1209;
  --text:#222;
  --muted:#666;
  --light:#f7f7f7;
  --white:#fff;
}
*{box-sizing:border-box;margin:0;padding:0}
html,body{width:1200px;height:3606px;overflow:hidden}
body{position:relative;font-family:'Montserrat',sans-serif;color:var(--text);background:var(--white)}
.abs{position:absolute}

/* header */
.topbar{left:470px;top:0;width:730px;height:38px;background:var(--sun);clip-path:polygon(0 0,100% 0,100% 100%,28px 100%);display:flex;align-items:center;padding-left:52px;font-size:13px;color:var(--ink)}
.topbar .item{display:flex;align-items:center;gap:8px;margin-right:54px}
.topbar .appt{border:2px solid var(--ink);padding:5px 14px;font-weight:500;margin-left:-8px}
.brand{display:flex;align-items:center;gap:10px;font-weight:700;color:var(--sun);font-size:34px;letter-spacing:1px;line-height:36px}
.brand .dot{width:22px;height:22px;border-radius:50%;background:var(--sun)}
.brand small{display:block;font-size:10px;letter-spacing:5px;color:var(--ink);font-weight:600;line-height:12px}
.nav{left:416px;top:62px;display:flex;font-size:13px;font-weight:600;color:var(--ink)}
.nav a{padding:9px 17px}
.nav a.active{background:var(--sun);color:#fff}

/* hero */
.hero{left:0;top:115px;width:1200px;height:550px;background:
  radial-gradient(ellipse 260px 200px at 930px 300px,#c9c2bb,transparent 70%),
  radial-gradient(ellipse 300px 260px at 560px 120px,#6a6661,transparent 70%),
  radial-gradient(ellipse 240px 180px at 380px 390px,#4e4b48,transparent 70%),
  linear-gradient(110deg,#57524d,#8a847e 45%,#9c958f 70%,#6a645e)}
.hero-title{left:0;top:268px;width:1200px;text-align:center;font-family:'Playfair Display',serif;font-weight:900;color:#fff;font-size:50px;line-height:58px;text-shadow:0 2px 8px rgba(0,0,0,.4)}
.btn-sun{background:var(--sun);color:#fff;font-size:13px;font-weight:600;display:flex;align-items:center;justify-content:center}
.dots{left:562px;top:598px;display:flex;gap:12px}
.dots span{width:16px;height:16px;border:2px solid #fff;border-radius:50%}
.dots span.on{background:radial-gradient(#fff 3px,transparent 4px)}

/* headings */
.heading{font-family:'Playfair Display',serif;font-weight:900;font-size:40px;color:var(--ink);letter-spacing:.5px;line-height:48px}
.heading em{font-style:normal;color:var(--sun)}

/* about */
.about-sub{left:90px;top:800px;width:490px;font-size:17px;font-weight:600;line-height:21px}
.about-text{left:90px;top:872px;width:500px;font-size:14px;line-height:20px;color:#333}
.btn-line{border:2px solid var(--ink);font-size:13px;font-weight:600;display:flex;align-items:center;justify-content:center;color:var(--ink)}

/* services */
.svc-img{width:322px;height:239px}
.svc-label{width:322px;text-align:center;color:#fff;font-size:16px;font-weight:600;letter-spacing:1px}
.svc-tag{left:827px;top:1610px;width:247px;height:57px;background:var(--sun);color:var(--ink);font-weight:600;font-size:16px;letter-spacing:1px;display:flex;align-items:center;justify-content:center}

/* team */
.card{top:2282px;width:238px;height:336px;background:#fff;border:1px solid #eee;text-align:center}
.card.focus{box-shadow:0 4px 18px rgba(0,0,0,.12);border-color:transparent}
.avatar{width:176px;height:176px;border-radius:50%;margin:16px auto 0;border:5px solid #e9e9e9}
.card.focus .avatar{border-color:var(--sun)}
.member{color:var(--sun);font-size:15px;font-weight:500;line-height:20px;margin-top:14px;padding:0 10px;height:42px;display:flex;align-items:center;justify-content:center}
.spec{font-size:12px;font-weight:500;margin-top:8px;color:#333}
.spec-text{font-size:11px;color:var(--muted);line-height:16px;margin-top:4px}

/* contact */
.contact{left:0;top:2795px;width:1200px;height:420px;background:var(--light)}
.c-item{display:flex;gap:14px}
.c-icon{width:35px;height:35px;border-radius:50%;background:var(--sun);flex:none;display:flex;align-items:center;justify-content:center}
.c-label{color:var(--sun);font-size:13px;line-height:16px}
.c-value{font-size:14px;font-weight:500;line-height:19px;color:#111}
.col{display:flex;flex-direction:column;gap:22px}

/* footer */
.f-title{font-family:'Playfair Display',serif;font-weight:700;color:var(--sun);font-size:19px;letter-spacing:.5px}
.f-links{list-style:none;margin-top:12px;font-size:13.5px;color:#fff;line-height:24px}
.f-links .cur{color:var(--sun);text-decoration:underline}
.bottom{left:0;top:3570px;width:1200px;height:36px;background:var(--sun);display:flex;align-items:center;justify-content:space-between;padding:0 88px;font-size:13px;color:#fff}
.social{display:flex;gap:18px}
.social span{width:12px;height:12px;border-radius:50%;background:#fff}
</style>
</head>
<body>

<div class="abs topbar">
  <span class="item"><svg width="12" height="12" viewBox="0 0 16 16"><path d="M3 1l3 3-2 2c1 2 3 4 5 5l2-2 3 3-2 3C7 15 1 9 1 3Z" fill="#1b1209"/></svg>555-010-2229</span>
  <span class="item"><svg width="13" height="10" viewBox="0 0 16 12"><rect width="16" height="12" fill="#1b1209"/><path d="M0 0l8 7 8-7" stroke="#F0B22A" fill="none"/></svg>info@dawnvaleobgyn.com</span>
  <span class="appt">Schedule an Appointment</span>
</div>
<div class="abs brand" style="left:90px;top:46px">
  <span class="dot"></span>
  <div>DAWNVALE<small>OB/GYN SERVICES</small></div>
</div>
<nav class="abs nav">
  <a class="active">HOME</a><a>OBSTETRICS</a><a>GYNAECOLOGY</a><a>NEWS</a><a>PATIENT EDUCATION</a><a>RESOURCES</a>
</nav>

<div class="abs hero" role="img" aria-label="Doctor pointing at an ultrasound monitor while scanning a smiling pregnant patient"></div>
<svg class="abs" style="left:0;top:560px" width="1200" height="110" viewBox="0 0 1200 110">
  <path d="M0 50 C300 120 900 120 1200 50 L1200 110 L0 110Z" fill="#fff"/>
  <path d="M310 40 Q600 -10 890 40 Q600 100 310 40Z" fill="#F0B22A"/>
</svg>
<div class="abs hero-title">WE'RE SPECIALIST<br>IN YOU!</div>
<div class="abs btn-sun" style="left:525px;top:400px;width:139px;height:37px">CONTACT US</div>
<div class="abs dots"><span></span><span class="on"></span><span></span></div>

<h2 class="abs heading" style="left:114px;top:734px"><em>ABOUT</em> US</h2>
<p class="abs about-sub">Lorem Ipsum is simply dummy text of the printing and typesetting industry.</p>
<div class="abs about-text">
  <p>Lorem Ipsum has been the industry's standard dummy text ever since the 1500s, when an unknown printer took a galley of type and scrambled it to make a type specimen book.</p>
  <p style="margin-top:20px">It has survived not only five centuries, but also the leap into electronic typesetting, remaining essentially unchanged...</p>
</div>
<div class="abs btn-line" style="left:89px;top:1033px;width:139px;height:39px">CONTACT US</div>
<svg class="abs" style="left:680px;top:715px" width="480" height="395" viewBox="0 0 480 395" role="img" aria-label="Smiling doctor with stethoscope performing an ultrasound scan">
  <defs>
    <radialGradient id="aboutFill" cx="0.55" cy="0.35" r="0.7">
      <stop offset="0" stop-color="#f1ece8"/>
      <stop offset="0.45" stop-color="#d6dde6"/>
      <stop offset="1" stop-color="#9fb0c4"/>
    </radialGradient>
  </defs>
  <path d="M60 240 C30 160 120 140 140 80 C170 10 280 0 320 60 C350 110 460 100 470 190 C478 270 360 280 300 320 C230 370 90 330 60 240Z" fill="url(#aboutFill)"/>
  <path d="M45 270 C20 170 130 150 150 70 C180 0 300 -5 330 70 C355 130 470 120 465 210 C460 290 350 280 290 340 C220 400 70 370 45 270Z" fill="none" stroke="#F0B22A" stroke-width="3"/>
</svg>

<svg class="abs" style="left:0;top:1170px" width="1200" height="900" viewBox="0 0 1200 900">
  <path d="M290 36 Q600 -12 905 36 Q600 20 290 36Z" fill="#F0B22A"/>
  <path d="M0 80 Q600 -15 1200 80 L1200 842 Q600 930 0 842Z" fill="#1b1209"/>
</svg>
<svg class="abs" style="left:0;top:2050px" width="1200" height="45" viewBox="0 0 1200 45">
  <path d="M285 6 Q600 60 910 6 Q600 32 285 6Z" fill="#F0B22A"/>
</svg>
<h2 class="abs heading" style="left:0;width:1200px;text-align:center;top:1300px;color:#fff"><em>OUR</em> SERVICES</h2>

<div class="abs svc-img" style="left:88px;top:1387px;background:radial-gradient(ellipse 120px 110px at 170px 90px,#8a8fa0,transparent 70%),radial-gradient(ellipse 90px 80px at 60px 70px,#3d3e44,transparent 70%),linear-gradient(160deg,#ece6dd,#cfc6ba 55%,#a49b90)" role="img" aria-label="Woman with a headache sitting on a sofa"></div>
<div class="abs svc-label" style="left:88px;top:1638px">MENOPAUSE</div>
<div class="abs svc-img" style="left:439px;top:1387px;background:radial-gradient(ellipse 90px 80px at 230px 80px,#2f5d94,transparent 70%),radial-gradient(ellipse 70px 120px at 70px 130px,#5a4536,transparent 70%),linear-gradient(135deg,#eef1f4,#c8d0da 60%,#9aa6b4)" role="img" aria-label="Doctor operating an ultrasound machine"></div>
<div class="abs svc-label" style="left:439px;top:1638px">ULTRASOUND</div>
<div class="abs svc-img" style="left:790px;top:1387px;background:radial-gradient(ellipse 110px 130px at 230px 150px,#3d72c4,transparent 70%),radial-gradient(ellipse 80px 120px at 40px 120px,#5b4a40,transparent 70%),linear-gradient(135deg,#dfe3e6,#c0c6cc)" role="img" aria-label="Doctor showing an ultrasound print to a patient"></div>
<div class="abs svc-tag">GYN EXAMS</div>

<div class="abs svc-img" style="left:88px;top:1693px;background:radial-gradient(ellipse 80px 70px at 160px 130px,#e8e8e6,transparent 70%),radial-gradient(ellipse 110px 160px at 40px 120px,#6f6258,transparent 70%),radial-gradient(ellipse 80px 160px at 290px 120px,#4e5a66,transparent 70%),linear-gradient(180deg,#b7c7cc,#9aa4a6)" role="img" aria-label="Couple holding tiny baby shoes"></div>
<div class="abs svc-label" style="left:88px;top:1945px">FAMILY PLANNING</div>
<div class="abs svc-img" style="left:439px;top:1693px;background:radial-gradient(ellipse 70px 70px at 120px 90px,#9cc6ea,transparent 70%),radial-gradient(ellipse 90px 80px at 230px 140px,#c79a82,transparent 70%),linear-gradient(135deg,#4b8ed2,#1f5aa2 60%,#163f78)" role="img" aria-label="Surgeons holding a newborn in the operating room"></div>
<div class="abs svc-label" style="left:439px;top:1945px">GYNECOLOGY SURGERY</div>
<div class="abs svc-img" style="left:790px;top:1693px;background:radial-gradient(ellipse 70px 120px at 60px 140px,#3fb99a,transparent 70%),radial-gradient(ellipse 60px 90px at 110px 170px,#4a3a32,transparent 70%),radial-gradient(ellipse 80px 130px at 270px 140px,#ecebea,transparent 70%),linear-gradient(135deg,#e8e2da,#bcb0a2)" role="img" aria-label="Doctor listening to a pregnant woman's belly with a stethoscope"></div>
<div class="abs svc-label" style="left:790px;top:1945px">OBSTETRICS</div>

<h2 class="abs heading" style="left:0;width:1200px;text-align:center;top:2194px"><em>OUR</em> TEAM</h2>

<div class="abs card" style="left:88px">
  <div class="avatar" role="img" aria-label="Portrait of Alan Brenner" style="background:radial-gradient(circle at 50% 45%,#d8b8a0 0,#c9a88f 30%,#f0efee 62%)"></div>
  <div class="member">ALAN BRENNER, M.D.</div>
  <div class="spec">SPECIALTY</div>
  <div class="spec-text">Normal and high-risk pregnancy,<br>Menopausal and Family Planning</div>
</div>
<div class="abs card" style="left:350px">
  <div class="avatar" role="img" aria-label="Portrait of Diana Rowell" style="background:radial-gradient(circle at 50% 45%,#e2c2ac 0,#6b4634 38%,#efeeed 64%)"></div>
  <div class="member">DIANA ROWELL<br>MSN, ARNP, CNM</div>
  <div class="spec">SPECIALTY</div>
  <div class="spec-text">Normal and high-risk pregnancy,<br>Menopausal and Family Planning</div>
</div>
<div class="abs card focus" style="left:611px">
  <div class="avatar" role="img" aria-label="Portrait of Marcus Tolliver" style="background:radial-gradient(circle at 50% 45%,#5a3a28 0,#3a2519 34%,#e9e8e7 62%)"></div>
  <div class="member">MARCUS TOLLIVER,<br>M.D., FACOG</div>
  <div class="spec">SPECIALTY</div>
  <div class="spec-text">Normal and high-risk pregnancy,<br>Menopausal and Family Planning</div>
</div>
<div class="abs btn-sun" style="left:661px;top:2600px;width:139px;height:37px">
  <svg width="30" height="12" viewBox="0 0 30 12"><path d="M0 6H28M22 1l6 5-6 5" stroke="#fff" stroke-width="2" fill="none"/></svg>
</div>
<div class="abs card" style="left:874px">
  <div class="avatar" role="img" aria-label="Portrait of Sandra E Fielding-Hart" style="background:radial-gradient(circle at 50% 45%,#f0d2bc 0,#c9a070 38%,#f2f1f0 64%)"></div>
  <div class="member">SANDRA E FIELDING-<br>HART, CNM, ARNP</div>
  <div class="spec">SPECIALTY</div>
  <div class="spec-text">Normal and high-risk pregnancy,<br>Menopausal and Family Planning</div>
</div>
<div class="abs btn-line" style="left:538px;top:2678px;width:124px;height:38px">VIEW ALL</div>

<div class="abs contact"></div>
<div class="abs col" style="left:88px;top:2893px">
  <div class="c-item"><span class="c-icon"><svg width="16" height="16" viewBox="0 0 16 16"><path d="M3 1l3 3-2 2c1 2 3 4 5 5l2-2 3 3-2 3C7 15 1 9 1 3Z" fill="#fff"/></svg></span><div><div class="c-label">Call</div><div class="c-value">555-010-2229</div></div></div>
  <div class="c-item"><span class="c-icon"><svg width="16" height="14" viewBox="0 0 16 14"><rect x="4" y="0" width="8" height="4" fill="#fff"/><rect x="0" y="5" width="16" height="6" rx="1" fill="#fff"/><rect x="4" y="9" width="8" height="5" fill="#fff"/></svg></span><div><div class="c-label">Fax</div><div class="c-value">555-010-2301</div></div></div>
  <div class="c-item"><span class="c-icon"><svg width="16" height="12" viewBox="0 0 16 12"><rect width="16" height="12" fill="#fff"/><path d="M0 0l8 7 8-7" stroke="#F0B22A" fill="none"/></svg></span><div><div class="c-label">Email</div><div class="c-value">info@dawnvaleobgyn.com</div></div></div>
  <div class="c-item"><span class="c-icon"><svg width="12" height="17" viewBox="0 0 12 17"><path d="M6 17C2 11 0 8 0 6a6 6 0 0112 0c0 2-2 5-6 11Z" fill="#fff"/><circle cx="6" cy="6" r="2" fill="#F0B22A"/></svg></span><div><div class="c-label">Address</div><div class="c-value">1200 Harbor Street<br>Suite 306 Lakeview,<br>Fl 33000</div></div></div>
</div>
<div class="abs col" style="left:392px;top:2893px">
  <div class="c-item"><span class="c-icon"><svg width="16" height="16" viewBox="0 0 16 16"><path d="M3 1l3 3-2 2c1 2 3 4 5 5l2-2 3 3-2 3C7 15 1 9 1 3Z" fill="#fff"/></svg></span><div><div class="c-label">Call</div><div class="c-value">555-010-2229</div></div></div>
  <div class="c-item"><span class="c-icon"><svg width="16" height="14" viewBox="0 0 16 14"><rect x="4" y="0" width="8" height="4" fill="#fff"/><rect x="0" y="5" width="16" height="6" rx="1" fill="#fff"/><rect x="4" y="9" width="8" height="5" fill="#fff"/></svg></span><div><div class="c-label">Fax</div><div class="c-value">555-010-6903</div></div></div>
  <div class="c-item"><span class="c-icon"><svg width="16" height="12" viewBox="0 0 16 12"><rect width="16" height="12" fill="#fff"/><path d="M0 0l8 7 8-7" stroke="#F0B22A" fill="none"/></svg></span><div><div class="c-label">Email</div><div class="c-value">info@dawnvaleobgyn.com</div></div></div>
  <div class="c-item"><span class="c-icon"><svg width="12" height="17" viewBox="0 0 12 17"><path d="M6 17C2 11 0 8 0 6a6 6 0 0112 0c0 2-2 5-6 11Z" fill="#fff"/><circle cx="6" cy="6" r="2" fill="#F0B22A"/></svg></span><div><div class="c-label">Address</div><div class="c-value">2900 Palm Road<br>Suite 101<br>Cedar Grove, Fl 33001</div></div></div>
</div>
<div class="abs" style="left:705px;top:2862px;width:407px;height:303px;background:radial-gradient(ellipse 40px 150px at 370px 150px,#f6d98a,transparent 70%),linear-gradient(135deg,#f1f2f4,#e4e7eb)" role="img" aria-label="Street map showing the office location"></div>

<svg class="abs" style="left:0;top:3180px" width="1200" height="426" viewBox="0 0 1200 426">
  <path d="M0 0 Q600 110 1200 0 L1200 426 L0 426Z" fill="#1b1209"/>
  <path d="M385 86 Q600 55 815 86 Q600 100 385 86Z" fill="#F0B22A"/>
</svg>
<div class="abs brand" style="left:96px;top:3420px">
  <span class="dot"></span>
  <div>DAWNVALE<small style="color:#fff">OB/GYN SERVICES</small></div>
</div>
<div class="abs" style="left:408px;top:3340px">
  <div class="f-title">QUICK LINKS</div>
  <ul class="f-links"><li class="cur">Home</li><li>Obstetrics</li><li>Gynaecology</li><li>News</li><li>Patient Education</li><li>Resources</li></ul>
</div>
<div class="abs" style="left:647px;top:3340px">
  <div class="f-title">OUR SERVICES</div>
  <ul class="f-links"><li>Menopause</li><li>Ultrasound</li><li>Gyn Exams</li><li>Family Planning</li><li>Gynecology Surgery</li><li>Obstetrics</li></ul>
</div>
<div class="abs" style="left:896px;top:3340px">
  <div class="f-title">HELPFUL LINKS</div>
  <ul class="f-links"><li>Office Forms</li><li>Office Policies</li><li>OB Guide</li><li>FAQ's</li></ul>
</div>
<div class="abs" style="left:1078px;top:3502px;width:34px;height:34px;border-radius:50%;background:var(--sun);display:flex;align-items:center;justify-content:center">
  <svg width="14" height="18" viewBox="0 0 14 18"><path d="M7 18V2M1 8l6-6 6 6" stroke="#111" stroke-width="2.4" fill="none"/></svg>
</div>
<div class="abs bottom">
  <span>© 2022 Dawnvale OB/GYN Services. All Right Reserved</span>
  <div class="social"><span></span><span></span><span></span><span></span></div>
</div>

</body>
</html>
```